Group Medical Practice needs stationery, business cards etc. designed

We need stationery designed for a multisite practice that offers primary medical, dental and behavioral healthcare. We would like a design that is consistent for letterhead, business cards, Microsoft Outlook stationery etc. We have attached our new logo design.

```html
<!DOCTYPE html>
<html lang="en">
<head>
<meta charset="utf-8">
<title>Cedar Ridge Health Services – Stationery</title>
<link href="https://fonts.googleapis.com/css2?family=Open+Sans:ital,wght@0,400;0,600;1,400&display=swap" rel="stylesheet">
<style>
  :root{
    --bg:#6f7682;
    --paper:#ffffff;
    --mist:#dde8f2;
    --brand-blue:#1f6fae;
    --brand-green:#7fb93a;
    --ink:#3a3f47;
    --ink-soft:#7a808a;
    --rule:#c9d3de;
    --faint:#e9eef3;
  }
  *{box-sizing:border-box;margin:0;padding:0}
  html,body{width:1200px;height:1000px;overflow:hidden}
  body{background:var(--bg);font-family:"Open Sans",Arial,sans-serif;color:var(--ink);position:relative}

  .sheet{position:absolute;background:var(--paper);box-shadow:0 6px 18px rgba(0,0,0,.25);overflow:hidden}
  .band{position:absolute;inset:0;width:100%;height:100%}

  .brand{position:absolute;display:flex;align-items:center;gap:6px;color:var(--brand-blue);font-weight:600;letter-spacing:.08em;text-transform:uppercase;white-space:nowrap}
  .brand-dot{width:9px;height:9px;border-radius:50%;background:var(--brand-green);flex:none}

  /* Envelope */
  .envelope{left:70px;top:60px;width:480px;height:240px}
  .envelope .brand{left:22px;top:24px;font-size:11px}
  .return-address{position:absolute;left:22px;top:50px;font-size:8px;line-height:1.5;color:var(--ink-soft)}

  /* Business cards */
  .card{width:350px;height:200px}
  .card-front{left:70px;top:370px}
  .card-front .brand{left:50%;top:58px;transform:translateX(-50%);font-size:14px}
  .card-front .tagline{position:absolute;left:0;right:0;top:84px;text-align:center;font-size:8px;letter-spacing:.2em;text-transform:uppercase;color:var(--brand-green)}
  .card-back{left:70px;top:610px}
  .card-back .person{position:absolute;left:26px;top:46px}
  .person-name{font-size:14px;font-weight:600;color:var(--brand-blue);letter-spacing:.06em;text-transform:uppercase}
  .person-role{font-size:9px;color:var(--ink-soft);margin-top:2px}
  .card-back .contact{position:absolute;left:26px;top:104px;font-size:9px;line-height:1.6;color:var(--ink)}
  .card-back .brand{right:20px;bottom:22px;font-size:9px}

  /* Letterhead */
  .letterhead{left:620px;top:56px;width:520px;height:736px}
  .letterhead .brand{right:36px;top:74px;font-size:15px}
  .letterhead .tagline{position:absolute;right:36px;top:96px;font-size:8px;letter-spacing:.22em;text-transform:uppercase;color:var(--brand-green)}
  .letter-body{position:absolute;left:58px;top:150px;width:370px;font-size:9.5px;line-height:1.55;font-style:italic;color:var(--ink)}
  .letter-body p{margin-bottom:10px}
  .signature{position:absolute;left:300px;top:420px;font-size:9px;font-style:italic;text-align:center;line-height:1.5}
  .signature .sig-name{border-top:1px solid var(--rule);padding-top:3px}
  .watermark{position:absolute;left:40px;top:560px;font-size:40px;font-weight:400;letter-spacing:.14em;text-transform:uppercase;color:var(--faint);white-space:nowrap}
  .letter-footer{position:absolute;left:40px;right:40px;bottom:40px;display:flex;align-items:center;gap:12px;font-size:8px;color:var(--ink-soft)}
  .letter-footer .footer-brand{color:var(--brand-blue);font-weight:600;letter-spacing:.08em;text-transform:uppercase;font-size:9px}
  .letter-footer .divider{width:1px;height:22px;background:var(--brand-blue)}
  .footer-rule{position:absolute;left:40px;right:40px;bottom:72px;height:1px;background:var(--rule)}
</style>
</head>
<body>

  <section class="sheet envelope" aria-label="Envelope">
    <svg class="band" viewBox="0 0 480 240" preserveAspectRatio="none" aria-hidden="true">
      <polygon points="0,0 170,0 190,70 130,110 0,110" fill="var(--mist)"/>
    </svg>
    <div class="brand"><span class="brand-dot"></span>Cedar Ridge</div>
    <div class="return-address">48 Orchard Lane Ste 210<br>Millbrook, Ohio 45001</div>
  </section>

  <section class="sheet card card-front" aria-label="Business card front">
    <svg class="band" viewBox="0 0 350 200" preserveAspectRatio="none" aria-hidden="true">
      <polygon points="0,0 350,0 350,40 260,100 200,70 130,110 0,60" fill="var(--mist)"/>
    </svg>
    <div class="brand"><span class="brand-dot"></span>Cedar Ridge</div>
    <div class="tagline">Health Services</div>
  </section>

  <section class="sheet card card-back" aria-label="Business card back">
    <svg class="band" viewBox="0 0 350 200" preserveAspectRatio="none" aria-hidden="true">
      <polygon points="0,0 350,0 350,24 0,24" fill="var(--mist)"/>
      <circle cx="310" cy="150" r="70" fill="var(--mist)"/>
    </svg>
    <div class="person">
      <div class="person-name">Daniel Hartwell</div>
      <div class="person-role">President and C.E.O</div>
    </div>
    <div class="contact">
      48 Orchard Lane Ste 210<br>
      Millbrook, Ohio 45001<br>
      (555) 014-2290
    </div>
    <div class="brand"><span class="brand-dot"></span>Cedar Ridge</div>
  </section>

  <section class="sheet letterhead" aria-label="Letterhead">
    <svg class="band" viewBox="0 0 520 736" preserveAspectRatio="none" aria-hidden="true">
      <polygon points="0,0 520,0 520,250 470,250 440,180 0,60" fill="var(--mist)"/>
    </svg>
    <div class="brand"><span class="brand-dot"></span>Cedar Ridge</div>
    <div class="tagline">Health Services</div>

    <div class="letter-body">
      <p>Lorem ipsum dolor sit amet, consectetur adipiscing elit. Donec nec purus luctus, pretium arcu sed, feugiat magna. Nullam vitae mauris in justo volutpat tempor. Cras gravida nisl at lacus commodo, vel dictum est finibus. Integer sed odio ac neque varius aliquet sit amet quis urna.</p>
      <p>Quisque dapibus sapien at tortor facilisis, non semper ligula blandit. Mauris a nisi et tellus interdum tristique. Sed ut magna vitae urna euismod convallis. Phasellus eget enim non risus faucibus posuere, ut placerat diam gravida.</p>
    </div>

    <div class="signature">
      <div class="sig-name">Daniel Hartwell</div>
      <div>President and C.E.O</div>
    </div>

    <div class="watermark">Cedar Ridge</div>
    <div class="footer-rule"></div>
    <footer class="letter-footer">
      <span class="footer-brand">Cedar Ridge</span>
      <span class="divider"></span>
      <span>48 Orchard Lane Ste 210 | Millbrook, Ohio 45001</span>
    </footer>
  </section>

</body>
</html>
```